New Business Card Design Project VORASTI-Italy

we are VORASTI-Italy
our company in the market for 3 years we are luxury cosmetic company and its about time for a facelift :)
i will like to have elegant luxurious and unique business card
that will give the person that get it a unique, luxurious and elegant impression
I'm VERY OPEN FOR NEW IDEAS , even duo i add a few files of things that i see on line and i like them

i add my logo as well
my website is VORASTI.COM
(if you would like to see the main style that we have)

Target Market(s)

adult that have money :)

Industry/Entity Type

Business

Contact Information for Business Card

Name - Paul Vorasti
Position - CEO and CO Founder
address - 4817 E Larkdale
telephone - 555-384-1962
email - paul@vorasti.com
fax - 555-384-1962
website - VORASTI.COM

Colors
000000
959595
fbee3e
ffffff

Requirements
Must have
• big logo in GOLD color
• elegant look
• impressive
Nice to have
• not must but maybe classy pattern background
• not must but maybe emblem
• maybe clear plastic business card
Should not have
• colors
• images

```html
<!DOCTYPE html>
<html lang="en">
<head>
<meta charset="utf-8">
<title>VORASTI Italy — Business Card</title>
<link rel="stylesheet" href="https://fonts.googleapis.com/css2?family=Tinos:wght@400;700&display=swap">
<style>
  :root {
    --backdrop: #1f1f1f;
    --card-black: #0c0c0c;
    --card-sheen: #1c1c1c;
    --frame-gold: #fbee3e;
    --foil-gold: #d8ad3c;
    --text-white: #ffffff;
    --text-grey: #959595;
  }
  * { box-sizing: border-box; margin: 0; padding: 0; }
  html, body {
    width: 1200px;
    height: 960px;
    overflow: hidden;
    background: var(--backdrop);
    font-family: "Tinos", "Times New Roman", serif;
  }
  .canvas {
    width: 1200px;
    height: 960px;
    display: flex;
    align-items: center;
    justify-content: center;
    gap: 80px;
  }
  .card {
    position: relative;
    width: 350px;
    height: 600px;
    background: linear-gradient(160deg, var(--card-sheen) 0%, var(--card-black) 55%, var(--card-sheen) 100%);
    box-shadow: 0 6px 0 -1px var(--foil-gold), 0 24px 40px rgba(0,0,0,0.55);
  }
  .card-frame {
    position: absolute;
    inset: 20px;
    border: 1.5px solid var(--frame-gold);
  }

  /* Front */
  .card--front .brand {
    position: absolute;
    left: 0; right: 0;
    top: 140px;
    display: flex;
    flex-direction: column;
    align-items: center;
    gap: 40px;
  }
  .brand-circle {
    width: 170px;
    height: 170px;
    border: 2px solid var(--foil-gold);
    border-radius: 50%;
  }
  .brand-name {
    color: var(--foil-gold);
    font-size: 40px;
    font-weight: 400;
    letter-spacing: 2px;
    text-align: center;
    line-height: 1.1;
  }
  .brand-name .brand-country {
    display: block;
    font-size: 14px;
    letter-spacing: 3px;
    margin-top: 6px;
  }

  /* Back */
  .card--back .person {
    position: absolute;
    left: 0; right: 0;
    top: 215px;
    text-align: center;
  }
  .person-name {
    color: var(--foil-gold);
    font-size: 38px;
    font-weight: 700;
    letter-spacing: 0.5px;
  }
  .person-role {
    color: var(--foil-gold);
    font-size: 15px;
    margin-top: 4px;
  }
  .contact {
    position: absolute;
    left: 48px;
    bottom: 52px;
    list-style: none;
    color: var(--text-white);
    font-size: 16px;
    line-height: 1.35;
    letter-spacing: 0.5px;
  }
</style>
</head>
<body>
  <main class="canvas">
    <section class="card card--front" aria-label="Card front">
      <div class="card-frame"></div>
      <div class="brand">
        <div class="brand-circle"></div>
        <p class="brand-name">VORASTI<span class="brand-country">ITALY</span></p>
      </div>
    </section>

    <section class="card card--back" aria-label="Card back">
      <div class="card-frame"></div>
      <div class="person">
        <h1 class="person-name">Paul Vorasti</h1>
        <p class="person-role">CEO and CO Founder</p>
      </div>
      <ul class="contact">
        <li class="contact-address">4817 E Larkdale</li>
        <li class="contact-phone">555-384-1962</li>
        <li class="contact-email">paul@vorasti.com</li>
      </ul>
    </section>
  </main>
</body>
</html>
```